Lawyer Needs New Atypical Stationery Design With Gravitas

I need new stationery (letterhead, envelopes, note pads, maybe business cards) for my law office. Although I work by myself, for myself, I need stationery that conveys strength, stability, and gravitas. I would also like a design that makes the end user think: "This is unique. I've never seen letterhead like this before." Most importantly, it should not look like many lawyers' letterhead, meaning no scales of justice. My current letterhead (attached) has my name and "Attorney at Law" on it; however, I would like to transition to "HASKE | LAW" or something like that with the new letterhead. Lastly, I would like an envelope design that is not the standard #10 envelope with a triangular back flap, maybe a square flap or something in the style or design that also makes people stop and think "That's different from anything I've seen before."

```html
<!DOCTYPE html>
<html lang="en">
<head>
<meta charset="utf-8">
<title>Haske | Law — Business Card</title>
<link href="https://fonts.googleapis.com/css2?family=Cinzel:wght@500;600;700&display=swap" rel="stylesheet">
<style>
  :root {
    --navy: #232161;
    --card: #ffffff;
    --band: #e6e6e6;
    --ink: #0c0c0c;
  }
  html, body {
    margin: 0;
    padding: 0;
    width: 1200px;
    height: 1200px;
    overflow: hidden;
    background: var(--navy);
  }
  .stage {
    width: 1200px;
    height: 1200px;
    display: block;
  }
  .card-face { fill: var(--card); }
  .accent-band { fill: var(--band); }
  .firm-name {
    font-family: "Cinzel", serif;
    font-weight: 600;
    font-size: 66px;
    fill: var(--ink);
  }
  .firm-title {
    font-family: "Cinzel", serif;
    font-weight: 600;
    font-size: 25px;
    fill: var(--ink);
    letter-spacing: 19px;
  }
  .contact-line {
    font-family: "Cinzel", serif;
    font-weight: 700;
    font-size: 28px;
    letter-spacing: 1.5px;
    fill: var(--ink);
  }
</style>
</head>
<body>
<svg class="stage" viewBox="0 0 1200 1200" xmlns="http://www.w3.org/2000/svg">
  <g class="business-card" transform="translate(101 301)">
    <rect class="card-face" x="0" y="0" width="998" height="598"/>
    <polygon class="accent-band" points="942,0 998,0 998,403 903,598 683,598"/>

    <text class="firm-name" x="218" y="195" textLength="561" lengthAdjust="spacingAndGlyphs">HASKE | LAW</text>
    <text class="firm-title" x="219" y="252" textLength="558" lengthAdjust="spacing">ATTORNEYATLAW</text>

    <g class="contact-block">
      <text class="contact-line" x="218" y="318">4120 MARLOW AVENUE</text>
      <text class="contact-line" x="218" y="351">SUITE TWO FIFTY</text>
      <text class="contact-line" x="218" y="384">WESTBROOK, CA 90412-1180</text>
      <text class="contact-line" x="218" y="417">T: (555) 014-6381</text>
      <text class="contact-line" x="218" y="450">E: OFFICE@HASKELAW.COM</text>
    </g>
  </g>
</svg>
</body>
</html>
```